Design a Full Page PDF Brochure "white paper" (Adobe InDesign)

Hello, my business needs a template to create "white papers" for our website. These are the free PDF downloads that you see on websites for lead capture.

The winning entry will need the following seven characteristics:
(1) A consistent color palette (or scheme) and feel of our website and logo (which I've attached). Even thought it is called a "white paper", please use lots of color and make it vibrant.
(2) A cover sheet that fills up the whole page, it also needs to have contact information on it (you can use this for now):

Ferris Oakhurst
48 Lindel Rd
Springfield, USA
414-362-8071
ferris@quabbleton.example
[login to view URL]

It's important that our logo is used as part of the cover page design. Feel free to be creative with this.

(3) The text needs to have different sized subheadings (H1, H2, H3)
(4) I would suggest adding "call outs" to highlight quotes from the text
(5) I would suggest submitting entries with multiple page layouts that can be used
(6) You may use Latin text and stock photos that I will replace. Our website [login to view URL] uses a theme of hiking, mountains, and paths.
(7) The final page needs to also have the contact information on it

To help clarify what I'm looking for, here are some examples of white papers:
[login to view URL]
[login to view URL]
[login to view URL]

The entries need to be in Adobe InDesign. The winner needs to turn over the final InDesign Files along with any supporting files such as in Adobe Illustrator.

Also, please do not contact me outside of Taskory (doing so will disqualify your entries).

Thank you ahead of time for your work.

```html
<!DOCTYPE html>
<html lang="en">
<head>
<meta charset="utf-8">
<title>Quabbleton Advisors — About Spread</title>
<link rel="stylesheet" href="https://fonts.googleapis.com/css2?family=Open+Sans:wght@400;700;800&family=Montserrat:wght@700&display=swap">
<style>
  :root {
    --backdrop: #dcd6d3;
    --paper: #ffffff;
    --green: #7cc242;
    --green-light: #a5d86b;
    --ink: #2b2b2b;
    --white: #ffffff;
    --sky: #8fb6d6;
    --slope: #5f8a3c;
  }
  html, body {
    margin: 0;
    width: 1200px;
    height: 832px;
    overflow: hidden;
    background: var(--backdrop);
    font-family: "Open Sans", Arial, sans-serif;
  }
  .spread {
    position: absolute;
    left: 80px;
    top: 66px;
    width: 1040px;
    height: 700px;
    display: flex;
    box-shadow: 0 8px 24px rgba(0,0,0,0.12);
  }
  .page {
    position: relative;
    width: 520px;
    height: 700px;
    overflow: hidden;
  }
  .page--left { background: var(--paper); }
  .page--right { background: var(--green); }

  .hero-photo {
    position: absolute;
    left: 0; top: 0;
    width: 180px; height: 700px;
    background: linear-gradient(180deg, var(--sky) 0%, #c9d9e6 28%, #7d9a6a 48%, var(--slope) 70%, #3f5f2a 100%);
  }
  .section-title {
    position: absolute;
    left: 205px;
    top: 400px;
    transform-origin: left top;
    transform: rotate(-90deg);
    margin: 0;
    font-family: "Montserrat", Arial, sans-serif;
    font-weight: 700;
    font-size: 22px;
    letter-spacing: 9px;
    color: var(--ink);
  }
  .mission-box {
    position: absolute;
    left: 240px;
    top: 264px;
    width: 280px;
    height: 140px;
    background: var(--green-light);
  }
  .mission-box p {
    margin: 0;
    padding: 14px 150px 0 14px;
    font-size: 9.5px;
    line-height: 1.45;
    font-weight: 700;
    color: var(--white);
  }
  .brand-band {
    position: absolute;
    left: 0;
    top: 264px;
    width: 190px;
    height: 140px;
    background: var(--paper);
    display: flex;
    align-items: center;
    justify-content: center;
    gap: 8px;
  }
  .brand-mark {
    width: 14px; height: 14px;
    background: var(--green);
  }
  .brand-name {
    font-size: 14px;
    font-weight: 700;
    color: var(--green);
  }
  .beliefs {
    position: absolute;
    left: 225px;
    top: 180px;
    width: 270px;
    color: var(--white);
    font-size: 8.5px;
    line-height: 1.5;
  }
  .beliefs ul {
    margin: 0 0 14px;
    padding-left: 12px;
  }
  .beliefs li { margin-bottom: 10px; }
  .beliefs .closing {
    margin: 0;
    font-weight: 800;
    font-size: 9.5px;
    line-height: 1.5;
  }
</style>
</head>
<body>
  <main class="spread">
    <section class="page page--left">
      <div class="hero-photo" role="img" aria-label="Photo of a hiker with a blue backpack looking over green mountain valleys and a lake"></div>
      <h1 class="section-title">ABOUT</h1>
      <div class="mission-box">
        <p>The mission of Quabbleton Advisors is to deliver truly comprehensive financial advice that is transparent, accountable, and wealth-optimized. This is what we believe:</p>
      </div>
    </section>
    <section class="page page--right">
      <div class="brand-band">
        <span class="brand-mark"></span>
        <span class="brand-name">Quabbleton</span>
      </div>
      <div class="beliefs">
        <ul>
          <li>We believe in providing strong leadership to our clients, and providing advice that is clear and comprehensive.</li>
          <li>We believe that service must be personalized, thorough, and exceeding expectations.</li>
          <li>We believe in the necessity to constantly educate and communicate with clients our best ideas, knowledge, and thoughts on informed planning.</li>
          <li>We believe that our core duty to clients is to advise them toward maximizing long-term growth while protecting present day buying needs.</li>
        </ul>
        <p class="closing">However clients may choose to measure us, we measure ourselves through our success in minimizing client worry. We see that the core worry that many people have is running out of money. Our job is to not only minimize this possibility, but to help them emotionally and intellectually feel financial freedom.</p>
      </div>
    </section>
  </main>
</body>
</html>
```